Venthrax - Joint website

Recently, three of our organizations: Norvelle, PRISM, and Talomir have united to work on a single project - Advanced Recycling of plastic waste via technology - Venthrax. For this united project, we need a new design of the website under the name of Venthrax which would feature the three companies.

Target Market(s)

Suppliers, consumers, and consumer brand companies within the Petrochemicals industry

Coding

Coded - Design and coding required

Number of Pages Required

1 page

Font styles to use
Other font styles liked:
• Lato

Requirements
Must have
• A clear image of how the Venthrax technology works/Sustainable aspect elaborated. The video on the home page featuring the three company representatives: https://www.examplevideo-host.com/watch?v=qTZP7LMWDA4&ab_channel=brightworkHelper
Nice to have
• Make use of icons, explained with some text for the technology. / make clear which role every company has within this initiative. / Picture of the first truck, with the banner of the three companies. / short video of the factory and technology.
Should not have
• A divided theme, it must be clear that it is a collaborated initiative, and that we all work together within our own expertise. / No cliché sustainability pictures, that aren’t relevant to the product.

```html
<!DOCTYPE html>
<html lang="en">
<head>
<meta charset="utf-8">
<title>Venthrax – Recycling of plastic waste</title>
<link rel="stylesheet" href="https://fonts.googleapis.com/css2?family=Lato:wght@400;700;900&family=Open+Sans:wght@600;700&display=swap">
<style>
:root{
  --ink:#222;
  --muted:#333;
  --white:#fff;
  --red:#d9421c;
  --orange:#e8731a;
  --amber:#efa21f;
  --grad:linear-gradient(90deg,#d9421c,#efa21f);
  --grad-v:linear-gradient(180deg,#f08a18,#d9421c);
  --dark:#5b5b5b;
  --card-dark:rgba(40,40,40,.88);
  --soft:#f7f7f7;
  --green:#3b8d3a;
  --navy:#1f4f8c;
}
*{box-sizing:border-box;margin:0;padding:0}
html,body{width:1200px;height:4073px;overflow:hidden}
body{font-family:"Lato",sans-serif;color:var(--ink);background:var(--white);position:relative}
.abs{position:absolute}
.grad-text{background:var(--grad);-webkit-background-clip:text;background-clip:text;color:transparent}
.btn{display:inline-flex;align-items:center;justify-content:center;border-radius:40px;font-weight:900;text-transform:uppercase;text-decoration:none}
.btn--grad{background:var(--grad);color:var(--white)}

/* header */
.site-header{top:0;left:0;width:1200px;height:110px;background:var(--white)}
.brand{left:172px;top:24px;font-size:54px;font-weight:700;color:#555;letter-spacing:-1px;line-height:60px}
.nav{right:172px;top:48px;display:flex;gap:10px;font-size:13px;text-transform:uppercase;color:var(--ink)}

/* hero */
.hero{top:110px;left:0;width:1200px;height:601px;background:linear-gradient(100deg,#b98c58 0%,#a67a4a 35%,#6f7a78 60%,#2a3a4f 100%)}
.hero__title{left:170px;top:95px;font-size:104px;font-weight:700;color:var(--white);letter-spacing:-2px;line-height:120px}
.hero__sub{left:170px;top:225px;font-family:"Open Sans",sans-serif;font-size:38px;font-weight:700;color:var(--white)}
.hero .btn{left:172px;top:318px;width:157px;height:66px;background:var(--white);color:var(--red);font-size:17px;box-shadow:0 4px 10px rgba(0,0,0,.25)}

/* challenges */
.converting{top:711px;left:0;width:1200px;height:897px;background:linear-gradient(180deg,#fff 0%,#fff 22%,#d6d3cf 45%,#8e8a84 75%,#6d6a66 100%)}
.section-title{width:1200px;text-align:center;font-size:32px;font-weight:900;line-height:42px;text-transform:uppercase}
.converting .section-title{top:96px}
.info-card{top:245px;width:412px;height:509px;background:var(--card-dark);border-radius:4px;color:var(--white);text-align:center;padding:46px 22px 0}
.info-card h3{font-size:27px;font-weight:700;margin:28px 0 18px;text-transform:uppercase}
.info-card p{font-size:13px;line-height:24px;margin-bottom:10px}
.info-card .lead{font-size:19px;line-height:30px;margin-bottom:18px}

/* how it works */
.how{top:1608px;left:0;width:1200px;height:842px;background:var(--white)}
.how .section-title{top:88px}
.cycle-svg{left:0;top:0}
.step-note{font-size:13px;line-height:21px;color:var(--ink)}
.node{width:118px;height:118px;border-radius:50%;background:var(--grad-v)}

/* products */
.products{top:2450px;left:0;width:1200px;height:535px;background:var(--soft)}
.video{left:172px;top:103px;width:482px;height:330px;background:linear-gradient(135deg,#3a2a1c,#7a5330 55%,#a8783f)}
.products h2{left:688px;top:125px;font-size:32px;font-weight:900}
.products p{left:688px;top:175px;width:340px;font-size:13px;line-height:22.5px;text-align:justify;color:var(--muted)}
.products .btn{left:688px;top:355px;width:130px;height:53px;font-size:14px}

/* partners */
.partners{top:2985px;left:0;width:1200px;height:625px;background:linear-gradient(100deg,#4b4b4b,#6b6a68 50%,#3f3f3f)}
.partners .section-title{top:88px;color:var(--white);font-weight:700}
.partner{top:188px;width:283px;height:340px;background:var(--grad-v);border-radius:4px}
.partner__inner{position:absolute;left:14px;top:22px;right:14px;bottom:0;background:var(--white);border-radius:4px;text-align:center;padding:30px 18px 0}
.partner--mid .partner__inner{top:0;bottom:22px}
.partner__name{height:70px;display:flex;align-items:center;justify-content:center;font-size:42px;font-weight:700}
.partner p{font-size:12.5px;line-height:24px;color:var(--muted);margin-top:16px}

/* footer */
.site-footer{top:3610px;left:0;width:1200px;height:463px;background:var(--dark);color:var(--white)}
.footer-brand{left:172px;top:100px;font-size:56px;font-weight:700;letter-spacing:-1px}
.footer-about{left:172px;top:190px;width:305px;font-size:13px;line-height:24px}
.footer-head{top:122px;font-size:22px;font-weight:400;text-transform:uppercase}
.quick-links{left:546px;top:165px;list-style:none;font-size:13px;line-height:27px}
.signup-input{left:780px;top:170px;width:248px;height:55px;border-radius:30px;background:var(--white);color:#555;font-size:13px;padding:20px 17px}
.site-footer .btn{left:780px;top:242px;width:121px;height:53px;font-size:14px}
.footer-rule{left:172px;top:355px;width:856px;height:2px;background:#bdbdbd}
.copyright{top:398px;width:1200px;text-align:center;font-family:"Open Sans",sans-serif;font-weight:600;font-size:16px}
</style>
</head>
<body>

<header class="site-header abs">
  <div class="brand abs">venthrax</div>
  <nav class="nav abs"><span>Home</span><span>Meet the partners</span><span>Technology</span><span>System and operations</span><span>Contact</span></nav>
</header>

<section class="hero abs" role="img" aria-label="Photo of a person in a green shirt collecting plastic bottles into a bag">
  <div class="hero__title abs">venthrax</div>
  <div class="hero__sub abs">Recycling of plastic waste</div>
  <a class="btn abs">Read more</a>
</section>

<section class="converting abs" role="img" aria-label="Photo of a large landfill of mixed plastic waste under a hazy sky">
  <h2 class="section-title abs grad-text">Converting waste to circular<br>resource!</h2>

  <article class="info-card abs" style="left:172px">
    <svg width="72" height="88" viewBox="0 0 72 88" fill="none" stroke="#fff" stroke-width="4" stroke-linecap="round">
      <path d="M24 58c0-10-12-14-12-30a24 24 0 0 1 48 0c0 16-12 20-12 30z"/>
      <path d="M26 66h20M28 74h16"/><rect x="30" y="78" width="12" height="6" fill="#fff"/>
      <path d="M8 8l4 4M64 8l-4 4M8 48l4-4M64 48l-4-4"/>
    </svg>
    <h3>Current challenges</h3>
    <p>1) Today polymers are the dominating materials for most applications in modern life. Global demand for polymers will double within the next 30 years.</p>
    <p>2) Compounds, additives, colorants and contaminants put the limits to the recycling of polymers. More than 50% of all polymer waste is rejected and incinerated.</p>
    <p>3) Our industry is failing to meet the sustainability goals set by the EU.</p>
  </article>

  <article class="info-card abs" style="left:616px">
    <svg width="88" height="88" viewBox="0 0 88 88" fill="none" stroke="#fff" stroke-width="4" stroke-linecap="round" stroke-linejoin="round">
      <circle cx="44" cy="14" r="8"/><path d="M30 44v-8a14 14 0 0 1 28 0v8"/>
      <path d="M6 30v26l14 16v12M82 30v26L68 72v12M14 40v14l12 12M74 40v14L62 66"/>
      <path d="M28 84V70l-8-10M60 84V70l8-10"/>
    </svg>
    <h3>Our solution!</h3>
    <p class="lead">Advanced Recycling via Venthrax<br>Technology!</p>
    <p>VENTHRAX's advanced depolymerisation technology allows the regeneration of a high quality liquid resource suitable for the production of new virgin quality polymers. It is applicable to mixed and contaminated plastics and of high efficiency.</p>
  </article>
</section>

<section class="how abs">
  <h2 class="section-title abs"><span style="color:var(--red)">How does</span> <span style="color:var(--orange)">it work?</span></h2>

  <p class="step-note abs" style="left:430px;top:175px;width:340px;text-align:center">A plastic product is produced and used by individual customers</p>
  <p class="step-note abs" style="left:172px;top:410px;width:131px;text-align:justify;text-align-last:right">After being used, the product is being disposed off</p>
  <p class="step-note abs" style="left:897px;top:410px;width:131px">The recycled oils are handled by the plastic product producer</p>
  <p class="step-note abs" style="left:430px;top:710px;width:340px;text-align:center">The waste is collected and processed via Venthrax's advanced recycling technology</p>

  <div class="node abs" style="left:541px;top:238px"></div>
  <div class="node abs" style="left:321px;top:383px"></div>
  <div class="node abs" style="left:767px;top:383px"></div>
  <div class="node abs" style="left:541px;top:568px"></div>

  <div class="abs" style="left:470px;top:412px;width:260px;text-align:center;font-size:58px;font-weight:700;color:#555;letter-spacing:-1px">venthrax</div>

  <svg class="cycle-svg abs" width="1200" height="842" viewBox="0 0 1200 842" fill="none">
    <defs><marker id="head" viewBox="0 0 10 10" refX="5" refY="5" markerWidth="5" markerHeight="5" orient="auto"><path d="M0 0L10 5L0 10z" fill="#111"/></marker></defs>
    <g stroke="#111" stroke-width="7" stroke-linecap="round" marker-end="url(#head)">
      <path d="M488 292C455 296 428 310 412 330"/>
      <path d="M785 340C772 318 752 300 718 292"/>
      <path d="M412 540C425 565 445 580 475 588"/>
      <path d="M720 610C750 600 770 580 780 555"/>
    </g>
    <g stroke="#fff" stroke-width="3.5" stroke-linejoin="round" stroke-linecap="round">
      <path d="M594 264h12v8l6 8v42h-24v-42l6-8z"/><path d="M588 292h24M588 306h24"/>
      <path d="M362 430h36M372 430v-6h16v6M366 436h28l-2 34h-24zM375 444v18M380 444v18M385 444v18"/>
      <path d="M806 466v-36h8v18l12-10v10l12-10v10l12-10v28zM812 456h6M824 456h6M836 456h6"/>
      <path d="M592 612l8-14 8 14M600 598l-10 0"/><path d="M584 628l-8 14h16M614 628l8 14h-16M603 642h-6"/>
    </g>
  </svg>
</section>

<section class="products abs">
  <div class="video abs" role="img" aria-label="Video of the three partner company representatives in a studio interview">
    <svg class="abs" style="left:215px;top:139px" width="52" height="52" viewBox="0 0 52 52"><circle cx="26" cy="26" r="24" fill="rgba(255,255,255,.25)" stroke="#fff" stroke-width="2"/><path d="M21 16l15 10-15 10z" fill="#fff"/></svg>
  </div>
  <h2 class="abs grad-text">OUR PRODUCTS</h2>
  <p class="abs">Nemo enim ipsam voluptatem quia voluptas sit aspernatur aut odit aut fugit, sed quia consequuntur magni dolores eos qui ratione voluptatem sequi nesciunt. Neque porro quisquam est, qui dolorem ipsum quia dolor sit amet, consectetur, adipisci velit, sed quia non numquam eius modi tempora incidunt ut labore et dolore magnam aliquam quaerat voluptatem.</p>
  <a class="btn btn--grad abs">Read more</a>
</section>

<section class="partners abs" role="img" aria-label="Photo of baled plastic waste beside a truck at a recycling yard">
  <h2 class="section-title abs">Partners in Venthrax</h2>

  <article class="partner abs" style="left:160px">
    <div class="partner__inner">
      <div class="partner__name" style="color:#111;font-weight:400">PRISM</div>
      <p>PRISM represents a diverse group of experts contributing to a sustainable future. We handle, trade, and explore commodities in energy, and renewables markets, with the aim to bring sustainability into a predominantly unsustainable market.</p>
    </div>
  </article>

  <article class="partner partner--mid abs" style="left:458px">
    <div class="partner__inner">
      <div class="partner__name" style="color:var(--green);font-weight:900;font-size:34px">NORVELLE</div>
      <p>NORVELLE specializes in lid films, rigid/flexible films and bags. Films are printed using flexographic, gravure and digital printing processes. Their aspiration is to find the optimal packaging solution for all kinds of products.</p>
    </div>
  </article>

  <article class="partner abs" style="left:757px">
    <div class="partner__inner">
      <div class="partner__name" style="color:var(--navy);font-size:34px">TALOMIR</div>
      <p>TALOMIR GmbH is with its engineers and technicians specialists in industrial plant engineering. Founded as a spin-off from a traditional German plant manufacturer, we develop and implement solutions for the growing demand for secondary.</p>
    </div>
  </article>
</section>

<footer class="site-footer abs">
  <div class="footer-brand abs">venthrax</div>
  <p class="footer-about abs">Sed ut perspiciatis unde omnis iste natus error sit voluptatem accusantium doloremque laudantium, totam rem aperiam. Nemo enim ipsam voluptatem quia voluptas sit aspernatur aut odit aut fugit, sed quia.</p>

  <h3 class="footer-head abs" style="left:546px">Quick links</h3>
  <ul class="quick-links abs"><li>Home</li><li>Meet the partners</li><li>Technology</li><li>System and Operations</li><li>Contact</li></ul>

  <h3 class="footer-head abs" style="left:778px">Newsletter signup</h3>
  <div class="signup-input abs">Email Address</div>
  <a class="btn btn--grad abs">Subscribe</a>

  <div class="footer-rule abs"></div>
  <p class="copyright abs">Copyrights @ 2021 Venthrax. All Rights Reserved.</p>
</footer>

</body>
</html>
```